Design for album cover

Looking for a creative design for an album cover for an unreleased song I wrote called "DRIFT". It's about regrets over a failed toxic relationship.
You can preview the song at the following link...
http://www.tunelofter.com/control_room/artist/5817402/songs

Reason: to allow designers to come up with better designs

```html
<!DOCTYPE html>
<html lang="en">
<head>
<meta charset="utf-8">
<title>Evan Marsh – Drift</title>
<link rel="stylesheet" href="https://fonts.googleapis.com/css2?family=Josefin+Sans:wght@300&display=swap">
<style>
  :root {
    --backdrop: #d9dadc;
    --cover-white: #fbfbfc;
    --ink: #1c1c1e;
    --smoke-blue: #6f86c9;
    --smoke-lilac: #9aa7dc;
    --smoke-teal: #8fc3d6;
  }
  * { margin: 0; padding: 0; box-sizing: border-box; }
  html, body {
    width: 1200px;
    height: 800px;
    overflow: hidden;
    background: var(--backdrop);
  }
  .canvas {
    position: relative;
    width: 1200px;
    height: 800px;
  }
  .album-cover {
    position: absolute;
    left: 280px;
    top: 80px;
    width: 640px;
    height: 640px;
    background: var(--cover-white);
    overflow: hidden;
    box-shadow: 0 6px 24px rgba(0, 0, 0, 0.12);
  }
  .smoke-art {
    position: absolute;
    left: 0;
    top: 220px;
    width: 640px;
    height: 420px;
    background:
      radial-gradient(ellipse 38% 30% at 22% 45%, rgba(111, 134, 201, 0.45), transparent 70%),
      radial-gradient(ellipse 30% 26% at 55% 60%, rgba(154, 167, 220, 0.40), transparent 70%),
      radial-gradient(ellipse 28% 24% at 86% 30%, rgba(143, 195, 214, 0.45), transparent 70%),
      radial-gradient(ellipse 40% 30% at 40% 90%, rgba(111, 134, 201, 0.35), transparent 70%),
      linear-gradient(to bottom, rgba(251, 251, 252, 0) 0%, rgba(154, 167, 220, 0.18) 100%);
  }
  .title-block {
    position: absolute;
    left: 76px;
    top: 118px;
    width: 470px;
    font-family: "Josefin Sans", sans-serif;
    font-weight: 300;
    color: var(--ink);
  }
  .artist-name {
    font-size: 50px;
    font-weight: 300;
    letter-spacing: 3px;
    line-height: 1;
    text-transform: uppercase;
    white-space: nowrap;
  }
  .title-rule {
    height: 1.5px;
    background: var(--ink);
    margin: 8px 0 14px;
  }
  .album-title {
    font-size: 96px;
    font-weight: 300;
    letter-spacing: 22px;
    line-height: 0.9;
    text-transform: uppercase;
    white-space: nowrap;
  }
</style>
</head>
<body>
  <main class="canvas">
    <section class="album-cover">
      <div class="smoke-art" role="img" aria-label="Wisps of blue and lilac smoke drifting across the lower half of the cover"></div>
      <div class="title-block">
        <p class="artist-name">Evan Marsh</p>
        <div class="title-rule"></div>
        <h1 class="album-title">Drift</h1>
      </div>
    </section>
  </main>
</body>
</html>
```